Business Cards and Stationery for Mediation Services Company
Business Cards and Startionery
Business Cards and Stationery for Mediation Services Company - Law
Creative Brief
Professional
Martin L. Crowe
Attorney-Mediator
5274 Harlow Ridge Ave. Suite 410 Dallas, Texas 75108
Mcrowe@BrimwoodCaseGroup.example
BrimwoodCaseGroup.example

```html
<!DOCTYPE html>
<html lang="en">
<head>
<meta charset="utf-8">
<title>Brimwood Case Group – Business Card</title>
<link rel="stylesheet" href="https://fonts.googleapis.com/css2?family=Lato:wght@400;700;900&display=swap">
<style>
  :root {
    --bg: #e4e6e8;
    --card: #ffffff;
    --blue: #2aa3d8;
    --blue-deep: #1b86bd;
    --green: #7ab648;
    --ink: #2b3a4a;
    --soft: #eef1f3;
    --faint: #cfe7f4;
  }
  * { margin: 0; padding: 0; box-sizing: border-box; }
  html, body { width: 1200px; height: 871px; overflow: hidden; }
  body {
    background: var(--bg);
    font-family: "Lato", Arial, sans-serif;
    color: var(--ink);
    display: flex; flex-direction: column; align-items: center;
    justify-content: center; gap: 24px;
  }
  .card {
    position: relative; width: 700px; height: 400px;
    background: var(--card); border-radius: 18px; overflow: hidden;
    box-shadow: 0 6px 18px rgba(0,0,0,.18);
  }
  .card svg.bands { position: absolute; inset: 0; }

  /* back */
  .card--back { background: linear-gradient(160deg, #ffffff 0%, var(--soft) 100%); }
  .back-mark {
    position: absolute; left: 40px; top: 40px;
    display: flex; align-items: center; gap: 22px;
  }
  .back-mark .dot { width: 150px; height: 150px; border-radius: 50%; background: var(--faint); }
  .back-mark .word { font-weight: 900; font-size: 150px; color: var(--faint); letter-spacing: 4px; line-height: 1; }
  .back-ident { position: absolute; left: 300px; top: 215px; }
  .back-ident .name { font-size: 28px; font-weight: 700; color: var(--blue); }
  .back-ident .role { font-size: 17px; font-weight: 700; color: var(--green); margin-top: 4px; }
  .back-ident .site { font-size: 16px; color: var(--blue); margin-top: 14px; }

  /* front */
  .brand { position: absolute; left: 0; right: 0; top: 54px; text-align: center; }
  .brand .dot { width: 46px; height: 46px; border-radius: 50%; background: var(--blue); margin: 0 auto 6px; }
  .brand .word { font-weight: 900; font-size: 54px; color: var(--blue); letter-spacing: 3px; line-height: 1; }
  .brand .rule { width: 230px; height: 2px; background: var(--green); margin: 8px auto 7px; }
  .brand .tagline { font-size: 12px; font-weight: 700; letter-spacing: 4px; color: var(--ink); }
  .contact {
    position: absolute; right: 34px; bottom: 26px;
    color: #fff; font-size: 14px; text-align: right; line-height: 1.75;
  }
  .contact .row { display: flex; justify-content: flex-end; align-items: center; gap: 10px; }
  .contact svg { width: 15px; height: 15px; flex: none; }
  .contact .pair { display: flex; gap: 60px; }
</style>
</head>
<body>
  <section class="card card--back" aria-label="Card back">
    <svg class="bands" viewBox="0 0 700 400" aria-hidden="true">
      <path d="M0 330 C 260 380 480 360 700 300 L700 400 L0 400 Z" fill="#f4f6f7"/>
    </svg>
    <div class="back-mark">
      <div class="dot"></div>
      <div class="word">BCG</div>
    </div>
    <div class="back-ident">
      <div class="name">Martin L. Crowe</div>
      <div class="role">Attorney-Mediator</div>
      <div class="site">BrimwoodCaseGroup.example</div>
    </div>
  </section>

  <section class="card card--front" aria-label="Card front">
    <svg class="bands" viewBox="0 0 700 400" aria-hidden="true">
      <defs>
        <linearGradient id="blueFill" x1="0" y1="0" x2="0" y2="1">
          <stop offset="0" stop-color="#36b1e4"/>
          <stop offset="1" stop-color="#1b86bd"/>
        </linearGradient>
      </defs>
      <path d="M0 262 C 250 250 480 210 700 120 L700 400 L0 400 Z" fill="#7ab648"/>
      <path d="M0 282 C 260 272 490 232 700 150 L700 400 L0 400 Z" fill="url(#blueFill)"/>
    </svg>
    <div class="brand">
      <div class="dot"></div>
      <div class="word">BCG</div>
      <div class="rule"></div>
      <div class="tagline">CLEAR PATHS FORWARD</div>
    </div>
    <div class="contact">
      <div class="row pair">
        <span>Mcrowe@BrimwoodCaseGroup.example</span>
        <span class="row">555-014-7392
          <svg viewBox="0 0 16 16"><path d="M3 1h3l1.5 4-2 1.3a8 8 0 0 0 4.2 4.2L11 8.5l4 1.5v3a2 2 0 0 1-2 2A12 12 0 0 1 1 3a2 2 0 0 1 2-2z" fill="#fff"/></svg>
        </span>
      </div>
      <div class="row">BrimwoodCaseGroup.example
        <svg viewBox="0 0 16 16"><circle cx="8" cy="8" r="6.5" fill="none" stroke="#fff" stroke-width="1.4"/><path d="M1.5 8h13M8 1.5c-3 3.5-3 9.5 0 13M8 1.5c3 3.5 3 9.5 0 13" fill="none" stroke="#fff" stroke-width="1.2"/></svg>
      </div>
      <div class="row">5274 Harlow Ridge Ave. Suite 410, Dallas, Texas 75108
        <svg viewBox="0 0 16 16"><path d="M8 15s5-5.2 5-9A5 5 0 0 0 3 6c0 3.8 5 9 5 9z" fill="#fff"/><circle cx="8" cy="6" r="1.8" fill="#1b86bd"/></svg>
      </div>
    </div>
  </section>
</body>
</html>
```